ATM BUSINESS MACHINES...

NEED A NEW LOGO AND BUSINESS CARD FOR A BRAND NEW ATM BUSINESS. WE GO TO LOCAL BUSINESSES AND PLACE ATM'S IN THER STORES FOR FREE. IT INCREASES THEIR BUSINESS. A VERY EYE CATCHY LOGO AND COLOR SCHEME...MODERN, PROFESSIONAL, YET MODERN AND APPEALING....

Target Market(s)

alll types of business owners...young & old....

Industry/Entity Type

Business

Contact Information for Business Card

PALMETTO QUICK FUNDS-ATM'S
" GET YOUR CASH NOW"
Ray T. Holbrook
President/Owner
P.O. Box 87
Hollow Pines, S.C. 29872
pqf.atm@zentromail.com
Free Atm's- Free Instalation, Free Maintenance Never a cost to business owner......Call now to get you free ATM and increase your sales......

Requirements
Nice to have
• $$$ signs.....colors....raised letters....
Maybe a logo PQF $$$ with ATM machine...

```html
<!DOCTYPE html>
<html lang="en">
<head>
<meta charset="utf-8">
<title>Palmetto Quick Funds – Business Card</title>
<link rel="stylesheet" href="https://fonts.googleapis.com/css2?family=Archivo+Black&family=Roboto+Condensed:wght@700&display=swap">
<style>
  :root {
    --brand-red: #d42127;
    --accent-red: #d8262c;
    --ink-black: #050505;
    --ink-charcoal: #2b2b2b;
    --white: #ffffff;
    --silver-light: #fafafa;
    --silver-mid: #c9c9c9;
    --silver-dark: #8a8a8a;
  }
  html, body {
    margin: 0;
    padding: 0;
    overflow: hidden;
    background: #ffffff;
  }
  .card {
    position: relative;
    width: 1200px;
    height: 702px;
    overflow: hidden;
    font-family: "Roboto Condensed", "Arial Narrow", sans-serif;
    font-weight: 700;
  }
  .card__top {
    position: absolute;
    inset: 0 0 auto 0;
    height: 337px;
    background: var(--brand-red);
  }
  .card__bottom {
    position: absolute;
    inset: 337px 0 0 0;
    background: linear-gradient(90deg, var(--ink-black) 0%, #161616 45%, var(--ink-charcoal) 100%);
  }
  .brand-mark {
    position: absolute;
    top: 62px;
    left: 0;
    width: 1200px;
    text-align: center;
    font-family: "Roboto Condensed", "Arial Narrow", sans-serif;
    font-weight: 700;
    font-size: 70px;
    line-height: 1;
    color: var(--white);
    letter-spacing: 2px;
  }
  .brand-name {
    position: absolute;
    top: 215px;
    left: 0;
    width: 1200px;
    text-align: center;
    margin: 0;
    font-family: "Archivo Black", "Arial Black", sans-serif;
    font-size: 47px;
    line-height: 1.2;
    letter-spacing: 1px;
    background: linear-gradient(180deg, var(--silver-light) 0%, var(--silver-mid) 55%, var(--silver-dark) 100%);
    -webkit-background-clip: text;
    background-clip: text;
    color: transparent;
    filter: drop-shadow(2px 2px 1px rgba(0,0,0,0.55));
  }
  .tagline {
    position: absolute;
    top: 286px;
    left: 0;
    width: 1200px;
    text-align: center;
    margin: 0;
    font-size: 37px;
    line-height: 1.1;
    color: var(--white);
  }
  .contact {
    position: absolute;
    top: 424px;
    left: 30px;
    width: 600px;
    text-align: center;
    font-size: 30px;
    line-height: 45px;
    color: var(--white);
  }
  .divider-red {
    position: absolute;
    left: 693px;
    top: 354px;
    width: 3px;
    height: 194px;
    background: linear-gradient(180deg, transparent, var(--brand-red) 30%, var(--brand-red) 70%, transparent);
  }
  .person {
    position: absolute;
    top: 418px;
    left: 712px;
    width: 400px;
    text-align: center;
    font-size: 31px;
    line-height: 45px;
    color: var(--white);
  }
  .offer {
    position: absolute;
    margin: 0;
    font-size: 29px;
    line-height: 1;
    color: var(--accent-red);
    white-space: nowrap;
  }
  .offer--left { top: 583px; left: 24px; }
  .offer--right { top: 583px; left: 471px; }
  .offer--call { top: 631px; left: 0; width: 1200px; text-align: center; }
  .divider-white {
    position: absolute;
    left: 443px;
    top: 555px;
    width: 3px;
    height: 84px;
    background: linear-gradient(180deg, transparent, #ffffff 50%, transparent);
  }
</style>
</head>
<body>
  <div class="card">
    <div class="card__top"></div>
    <div class="card__bottom"></div>

    <div class="brand-mark">PQF</div>
    <h1 class="brand-name">PALMETTO QUICK FUNDS-ATM'S</h1>
    <p class="tagline">($ GET YOUR CASH NOW $)</p>

    <div class="contact">
      <div>P.O. Box 87 Hollow Pines, S.C. 29872</div>
      <div>pqf.atm@zentromail.com</div>
    </div>

    <div class="divider-red"></div>

    <div class="person">
      <div>Ray T. Holbrook</div>
      <div>President/Owner</div>
    </div>

    <p class="offer offer--left">Free Atm's- Free Instalation</p>
    <div class="divider-white"></div>
    <p class="offer offer--right">Free Maintenance Never a cost to business owner</p>
    <p class="offer offer--call">Call now to get you free ATM and increase your sales</p>
  </div>
</body>
</html>
```